The Polish & Glow Studio Website Update

Hello. I am seeking to freshen up my website with a clean and easy feel that incorporates our modern chic style. Our services cater to mostly young professionals and modern moms.

We focus on natural nail care and gentle professional waxing. We are known for our cleanliness. Our clients like our current website, however I'm hoping to make it look even more professional and user friendly. Some clients have even said our current website feels welcoming, unlike other websites that in they feel give a snobbish vibe. I like clean lines, simple, fresh, and sometimes bold. Totally NOT a fan of whimsical.

I threw added an accent color to the color pallet...however it should be used in moderation. I am also open to other accent colors. I'd like the site to emphasize the Brazilian wax as much as nails, if not more than nail. The photos downloaded are just to give you a few images of who we are, however are not necessary. Current website www.thepolishandglowstudio.example

Target Market(s)

Females 30-55

Industry/Entity Type

Beauty Salon

Coding

Coded - Design and coding required

Number of Pages Required

5+ page

Font styles to use
Sans Serif

Colors
ffffff
1b1b1b
acd136
eeeeee
878787
c4c4c4
efefef
7f7f7f

Requirements
Must have
• Clean look
Nice to have
• Our logo
Should not have
• Whimsical

```html
<!DOCTYPE html>
<html lang="en">
<head>
<meta charset="utf-8">
<title>The Polish &amp; Glow Studio</title>
<link rel="stylesheet" href="https://fonts.googleapis.com/css2?family=Source+Sans+3:wght@400;600;700&display=swap">
<style>
:root{
  --white:#ffffff;
  --ink:#1b1b1b;
  --accent:#acd136;
  --panel:#efefef;
  --page:#e6e6e6;
  --nav:#a2a2a2;
  --muted:#878787;
  --rule:#d6d6d6;
  --dark:#333333;
  --darker:#232323;
}
*{box-sizing:border-box;margin:0;padding:0}
html,body{width:1200px;height:2247px;overflow:hidden}
body{background:var(--page);font-family:"Source Sans 3",Arial,sans-serif;color:var(--ink);position:relative}
.abs{position:absolute}
.site{position:absolute;left:132px;top:0;width:932px;height:2247px;background:var(--panel)}
/* top bar */
.topbar{left:0;top:0;width:932px;height:54px;background:var(--dark)}
.topbar a{position:absolute;top:19px;color:var(--white);font-size:13px;text-decoration:none;letter-spacing:.2px}
.search{position:absolute;left:676px;top:10px;width:214px;height:33px;background:#5a5a5a;color:var(--white);font-size:13px;padding:8px 0 0 15px}
.search svg{position:absolute;right:16px;top:7px}
/* brand */
.brand{left:0;top:54px;width:932px;height:114px;background:#f2f2f2;text-align:center;padding-top:36px;font-size:32px;font-weight:400;color:#555;letter-spacing:-.3px}
/* nav */
.mainnav{left:0;top:168px;width:932px;height:81px;background:var(--nav)}
.mainnav .active{position:absolute;left:133px;top:0;width:132px;height:81px;background:var(--accent)}
.nav-item{position:absolute;transform:translate(-50%,-50%);top:40px;color:var(--white);font-size:12.5px;text-transform:uppercase;text-align:center;line-height:16px;white-space:nowrap}
/* welcome */
.welcome-title{left:0;top:270px;width:932px;text-align:center;font-size:31px;font-weight:700;letter-spacing:.5px}
.welcome-sub{left:0;top:315px;width:932px;text-align:center;font-size:16px;font-weight:600;color:var(--accent)}
.welcome-text{left:138px;top:345px;width:630px;text-align:center;font-size:13.3px;line-height:16.5px;color:var(--muted)}
.slider{left:138px;top:463px;width:630px;height:247px;border-radius:0 0 22px 0;background:linear-gradient(120deg,#9a9696 0%,#5b5757 35%,#c79d90 65%,#3a3737 100%)}
.dots{display:flex;gap:6px}
.dot{width:15px;height:15px;border:2px solid var(--white)}
.dot.on{background:var(--accent)}
.rule{left:43px;width:846px;height:3px;background:var(--rule)}
/* mission */
.mission-frame{left:70px;top:828px;width:202px;height:325px;background:var(--white)}
.mission-photo{position:absolute;left:9px;top:15px;width:184px;height:295px;background:linear-gradient(160deg,#e7dcd6 0%,#f1e6e2 40%,#e9a0b0 75%,#c89a70 100%)}
.sec-title{font-size:31px;font-weight:700;letter-spacing:.2px}
.mission-text{left:298px;top:884px;width:306px;font-size:13.3px;line-height:16.5px;color:var(--muted)}
.mission-text p+p{margin-top:16px}
.services-list{left:651px;top:880px;list-style:none;font-size:12.5px;line-height:21.2px}
.services-list li{color:#6f8c1a;text-decoration:underline}
.btn{display:block;background:var(--accent);color:var(--white);font-size:12.5px;text-align:center}
/* hero */
.hero{left:0;top:1251px;width:932px;height:502px;background:linear-gradient(180deg,#6e6965 0%,#85807c 50%,#938f8b 100%)}
.hero-text{position:absolute;left:140px;top:219px;width:652px;text-align:center;color:var(--white);font-size:12.5px;line-height:17px}
.hero .btn{position:absolute;left:424px;top:278px;width:87px;height:33px;line-height:33px;font-size:13px}
.hero .dots{position:absolute;left:423px;top:439px}
.hero-shadow{left:20px;top:1753px;width:892px;height:40px;background:radial-gradient(ellipse at top,rgba(0,0,0,.14),rgba(0,0,0,0) 70%)}
/* footer */
.footer{left:0;top:1849px;width:932px;height:331px;background:var(--dark);color:var(--white)}
.footer h3{position:absolute;top:35px;font-size:21px;font-weight:600;letter-spacing:.3px;text-transform:uppercase}
.footer ul{position:absolute;top:70px;list-style:none;font-size:15px;line-height:26.4px}
.footer address{position:absolute;top:70px;font-style:normal;font-size:15px;line-height:19.5px}
.social{position:absolute;left:752px;top:74px;display:flex;gap:9px}
.social span{width:27px;height:27px;border-radius:50%;background:var(--white)}
.legal{left:0;top:2180px;width:932px;height:67px;background:var(--darker);color:var(--white);font-size:12.5px;padding:27px 0 0 44px}
</style>
</head>
<body>
<div class="site">
  <header class="abs topbar">
    <a href="#" style="left:44px">LOGIN</a>
    <a href="#" style="left:114px">REGISTER</a>
    <div class="search">Search
      <svg width="22" height="20" viewBox="0 0 22 20"><circle cx="8" cy="8" r="6" fill="none" stroke="#fff" stroke-width="2"/><line x1="12.5" y1="12.5" x2="20" y2="18" stroke="#fff" stroke-width="3" stroke-linecap="round"/></svg>
    </div>
  </header>

  <div class="abs brand">The Polish &amp; Glow Studio</div>

  <nav class="abs mainnav">
    <div class="active"></div>
    <span class="nav-item" style="left:76px">Home</span>
    <span class="nav-item" style="left:199px">Schedule<br>an appointment</span>
    <span class="nav-item" style="left:344px">Products<br>and services</span>
    <span class="nav-item" style="left:454px">Carrers</span>
    <span class="nav-item" style="left:550px">Specials</span>
    <span class="nav-item" style="left:656px">About us</span>
    <span class="nav-item" style="left:743px">FAQ</span>
    <span class="nav-item" style="left:831px">Contact us</span>
  </nav>

  <h1 class="abs welcome-title">WELCOME!</h1>
  <p class="abs welcome-sub">There are many variations of passages of Lorem Ipsum available,</p>
  <p class="abs welcome-text">Lorem Ipsum is simply dummy text of the printing and typesetting industry. Lorem Ipsum has been the industry's standard dummy text ever since the 1500s, when an unknown printer took a galley of type and scrambled it to make a type specimen book. It has survived not only five centuries, but also the leap into electronic typesetting, remaining essentially unchanged. It was popularised in the 1960s with the release of Letterline sheets containing Lorem Ipsum passages, and more recently with desktop publishing software like Pagewright Layout including versions of Lorem Ipsum.</p>

  <div class="abs slider" role="img" aria-label="Close-up of decorated nails with silver jewel nail art">
    <div class="dots" style="position:absolute;left:20px;top:212px"><span class="dot"></span><span class="dot"></span><span class="dot on"></span><span class="dot"></span></div>
  </div>

  <div class="abs rule" style="top:772px"></div>

  <div class="abs mission-frame"><div class="mission-photo" role="img" aria-label="Hands with pink manicured nails resting on a soft towel with rose petals"></div></div>
  <h2 class="abs sec-title" style="left:298px;top:835px">OUR MISSION</h2>
  <div class="abs mission-text">
    <p>To be the #1 nail and wax salon in the Brookfield, CT area, offering the most meticulous manicures, pedicures, and waxing service. We use superior products, advanced techniques, and exceptional sanitation procedures to provide our clients with safe, quality services. Our knowledgeable and friendly staff is always happy to assist with any of your Polish &amp; Glow concerns.</p>
    <p>We are excited to welcome another Licensed Nail Technician to our team, Dana Whitcombe. Dana has over 25 years experience and is also a certified Medical Nail Technician. You will love her spunk and genuine friendliness. If you're seeking a perfect mani, Dana is your girl.</p>
  </div>

  <h2 class="abs sec-title" style="left:645px;top:835px">OUR SERVICES</h2>
  <ul class="abs services-list">
    <li>~Nails~</li>
    <li>Signature Manicure- $24</li>
    <li>Gel Polish Manicure - $34</li>
    <li>Signature Pedicure - $40</li>
    <li>~Wax~</li>
    <li>Brow Design - $13</li>
    <li>Chin - $10</li>
    <li>Lip - $10</li>
    <li>Brazilian $55</li>
  </ul>
  <a class="abs btn" style="left:651px;top:1085px;width:125px;height:27px;line-height:27px">See More Services</a>

  <div class="abs rule" style="top:1200px"></div>

  <section class="abs hero" role="img" aria-label="Pair of hands with French manicured nails on a white towel">
    <p class="hero-text">Facials are now available at The Polish &amp; Glow Studio. Our Signature Facial is meticulously customized to your skin's needs, be it quenching your skin's thirst, clearing unflattering breakouts, or repairing sun damage and fine lines.</p>
    <a class="btn">BOOK NOW</a>
    <div class="dots"><span class="dot"></span><span class="dot"></span><span class="dot on"></span><span class="dot"></span></div>
  </section>
  <div class="abs hero-shadow"></div>

  <footer class="abs footer">
    <h3 style="left:45px">Quick Links</h3>
    <ul style="left:51px">
      <li>Home</li><li>SCHEDULEAN APPOINTMENT</li><li>PRODUCTS AND SERVICES</li><li>CARRERS</li><li>SPECIALS</li><li>ABOUT US</li><li>FAQ</li><li>CONTACT US</li>
    </ul>
    <h3 style="left:292px">Services</h3>
    <ul style="left:294px">
      <li>~Nails~</li><li>Signature Manicure- $24</li><li>Gel Polish Manicure - $34</li><li>Signature Pedicure - $40</li><li>~Wax~</li><li>Brow Design - $13</li><li>Chin - $10</li><li>Lip - $10</li><li>Brazilian $55</li>
    </ul>
    <h3 style="left:509px">Contact Us</h3>
    <address style="left:512px">The Polish &amp; Glow Studio<br>42 Elm Lane<br>Brookfield, CT 06804<br>ph: (203) 555-0148<br>info@thepolishandglowstudio.example</address>
    <h3 style="left:746px">Social Media</h3>
    <div class="social"><span></span><span></span><span></span><span></span></div>
  </footer>
  <div class="abs legal">Copyright 2016 The Polish &amp; Glow Studio. All rights reserved.</div>
</div>
</body>
</html>
```